Employees at R&T Gale Power Services need new modern business cards

We need new business cards that showcase our new rebranded logo. We are seeking modern, clean, fresh, attractive cards while still being professional. We want to stand out. A little bit about us: we work in Canada and the USA. We offer Technical Field Advisors to support wind turbine manufacturers through the construction phase of wind farms. I am attaching a mock inspiration picture to lead you in the direction we want to see this go. Also, FYI We have approx. 10/11 different employees that would need their own card. Let me know when you would need everyone's name. We would love to see some black and white options as well as color copies- when using colors we want green to be the dominant color with accents for blue and orange (colors should match our logo). I have also attached copies of our old business card for reference.

Contact Information for Business Card

Name, Telephone, Email, address, company name, website. EXAMPLE: Dean Whitlock, DeanWhitlock@randtgale.net, 555-384-9162, 318276 Fallow Line #7, Marrowby, ON X9Z 4Q2, www.randtgale.net

Colors
0054AA
0677BA
7BADD7
CADEEF
E8F1F8
00AB8E
00BBA5
67D7C9
C6EFE9
E9F9F6
F0912C
F2A743
F7CA91
FBE8D2
FDF5EE

Requirements
Must have
• 2 sided business card

```html
<!DOCTYPE html>
<html lang="en">
<head>
<meta charset="utf-8">
<title>R&amp;T Gale Power Services – Business Card</title>
<link href="https://fonts.googleapis.com/css2?family=Open+Sans:wght@400;600;700&display=swap" rel="stylesheet">
<style>
  :root {
    --stage: #2a2d33;
    --card: #141414;
    --card-edge: #0b0b0b;
    --text-light: #e6e6e6;
    --brand-blue: #0a7bc8;
    --brand-orange: #f5a623;
    --brand-green: #3bb54a;
    --emboss-light: #2b2b2b;
    --emboss-mid: #1d1d1d;
    --emboss-dark: #0e0e0e;
  }
  * { margin: 0; padding: 0; box-sizing: border-box; }
  html, body {
    width: 1200px; height: 900px; overflow: hidden;
    background: var(--stage);
    font-family: "Open Sans", sans-serif;
  }
  .canvas {
    width: 1200px; height: 900px;
    display: flex; align-items: center; justify-content: center; gap: 40px;
  }
  .card {
    position: relative;
    width: 540px; height: 309px;
    background: var(--card);
    border-radius: 4px;
    overflow: hidden;
    box-shadow: 0 14px 30px rgba(0,0,0,0.45), 0 0 0 1px var(--card-edge);
  }
  .card-front .corner-bands { position: absolute; left: 0; top: 0; }
  .contact-block {
    position: absolute; left: 104px; top: 70px;
    color: var(--text-light);
    font-size: 12.5px; line-height: 19px;
  }
  .contact-block .address { margin-bottom: 6px; }
  .contact-line { display: flex; align-items: center; gap: 8px; }
  .contact-line svg { width: 10px; height: 10px; flex: none; }
  .brand-wordmark {
    position: absolute;
    display: flex; align-items: center; gap: 9px;
  }
  .brand-dot {
    width: 22px; height: 22px; border-radius: 50%;
    background: var(--brand-green); flex: none;
  }
  .brand-name {
    color: var(--brand-green);
    font-weight: 700; font-size: 14px; line-height: 18px;
    text-transform: uppercase; letter-spacing: 0.4px;
    white-space: nowrap;
  }
  .card-front .brand-wordmark { left: 268px; top: 168px; }
  .person-name {
    position: absolute; left: 268px; top: 212px;
    color: var(--brand-blue);
    font-size: 24px; font-weight: 400; line-height: 30px;
    text-transform: uppercase; letter-spacing: 0.5px;
    white-space: nowrap;
  }
  .edge-tab {
    position: absolute; right: 0; bottom: 22px;
    width: 18px; height: 22px; background: var(--brand-green);
  }
  .emboss-field {
    position: absolute; inset: 0;
    background:
      radial-gradient(ellipse at 25% 25%, var(--emboss-light) 0%, transparent 55%),
      radial-gradient(ellipse at 70% 40%, var(--emboss-mid) 0%, transparent 60%),
      linear-gradient(160deg, var(--emboss-mid), var(--emboss-dark));
  }
  .card-back .brand-wordmark { left: 296px; top: 176px; }
</style>
</head>
<body>
<main class="canvas">

  <section class="card card-front" aria-label="Card front">
    <svg class="corner-bands" width="180" height="309" viewBox="0 0 180 309" aria-hidden="true">
      <polygon points="0,0 150,0 72,95 0,122" fill="var(--brand-blue)"/>
      <polygon points="150,0 176,0 72,95" fill="var(--brand-orange)"/>
      <polygon points="0,122 72,95 30,309 0,309" fill="var(--brand-green)"/>
    </svg>

    <div class="contact-block">
      <p class="address">318276 Fallow Line #7<br>Marrowby, ON X9Z 4Q2</p>
      <p class="contact-line">
        <svg viewBox="0 0 10 10" aria-hidden="true"><path d="M2 0.5 L3.6 2.8 L2.7 3.8 Q3.8 6 6.2 7.3 L7.2 6.4 L9.5 8 L8.3 9.5 Q3 9 0.5 1.7 Z" fill="var(--brand-orange)"/></svg>
        555-384-9162
      </p>
      <p class="contact-line">
        <svg viewBox="0 0 10 10" aria-hidden="true"><rect x="0.5" y="2" width="9" height="6.5" fill="var(--brand-orange)"/><polyline points="0.5,2 5,5.6 9.5,2" fill="none" stroke="var(--card)" stroke-width="0.9"/></svg>
        DeanWhitlock@randtgale.net
      </p>
      <p class="contact-line">
        <svg viewBox="0 0 10 10" aria-hidden="true"><circle cx="5" cy="5" r="4.5" fill="var(--brand-orange)"/><path d="M0.5 5 H9.5 M5 0.5 V9.5 M5 0.5 Q2 5 5 9.5 M5 0.5 Q8 5 5 9.5" stroke="var(--card)" stroke-width="0.7" fill="none"/></svg>
        www.randtgale.net
      </p>
    </div>

    <div class="brand-wordmark">
      <span class="brand-dot" aria-hidden="true"></span>
      <span class="brand-name">R&amp;T Gale Power Services</span>
    </div>

    <p class="person-name">Dean Whitlock</p>
    <span class="edge-tab" aria-hidden="true"></span>
  </section>

  <section class="card card-back" aria-label="Card back">
    <div class="emboss-field" role="img" aria-label="Full-card embossed pattern: rows of the brand symbol blind-debossed in black on black, catching light toward the upper left"></div>
    <div class="brand-wordmark">
      <span class="brand-dot" aria-hidden="true"></span>
      <span class="brand-name">R&amp;T Gale Power Services</span>
    </div>
  </section>

</main>
</body>
</html>
```